Young, modern, highly skilled carpenter needs business card design

I need a business card design for my construction business. Its called 'Pemberton Building Partners'. Im looking for a ultra modern design that incorporates P B P, the first letters of the name with only a subtle reference to carpentry. The design should reflect my high quality work and eye for detail. i have also uploaded some exmaple designs i like.

Industry/Entity Type

Construction

Requirements
Must have
• Name of business, my name, mobile number, ABN number, email address
Nice to have
• A logo incorporating the name of the business

```html
<!DOCTYPE html>
<html lang="en">
<head>
<meta charset="utf-8">
<title>Pemberton Building Partners – Business Card Concepts</title>
<link rel="stylesheet" href="https://fonts.googleapis.com/css2?family=Open+Sans:wght@400;700&family=Roboto+Condensed:wght@700&family=Tinos&display=swap">
<style>
  :root {
    --blue: #1f6ead;
    --yellow: #fcd200;
    --black: #000000;
    --white: #ffffff;
    --page: #ffffff;
    --shadow: rgba(0, 0, 0, 0.55);
  }
  * { box-sizing: border-box; margin: 0; padding: 0; }
  html, body { width: 927px; height: 1200px; overflow: hidden; background: var(--page); }
  .sheet { position: relative; width: 927px; height: 1200px; }

  .card {
    position: absolute;
    width: 385px;
    height: 212px;
    overflow: hidden;
    box-shadow: 7px 7px 6px var(--shadow);
    font-family: "Open Sans", Arial, sans-serif;
  }
  .card--blue { background: var(--blue); }
  .card--yellow { background: var(--yellow); }
  .card--black { background: var(--black); }
  .card--white { background: var(--white); border: 1px solid #d8d8d8; }

  .side-label {
    position: absolute;
    font-family: "Tinos", "Times New Roman", serif;
    font-size: 17px;
    color: var(--black);
  }

  .abs { position: absolute; white-space: nowrap; }

  .mark {
    font-family: "Roboto Condensed", "Arial Narrow", sans-serif;
    font-weight: 700;
    line-height: 1;
  }
  .mark--initials { font-size: 46px; letter-spacing: 1px; }
  .mark--name { font-size: 17px; }
  .mark--initials-sm { font-size: 33px; }
  .mark--name-sm { font-size: 12.5px; }

  .hand-art { position: absolute; }

  .contact { position: absolute; font-size: 10.5px; line-height: 13.5px; color: var(--white); }
  .contact .person { font-size: 13px; font-weight: 700; line-height: 16px; }
  .contact .role { margin-bottom: 13px; }
  .contact .address { margin-bottom: 8px; }
  .contact .details {
    display: grid;
    grid-template-columns: 52px auto;
    column-gap: 2px;
    margin-bottom: 10px;
  }
  .contact .details dt { font-weight: 700; white-space: nowrap; }
  .contact .details dd { white-space: nowrap; }
  .contact .details dd.strong { font-weight: 700; }
  .contact--gold .person,
  .contact--gold .details dt { color: var(--yellow); }

  .web { position: absolute; font-size: 10.5px; font-weight: 700; }

  .saw-art { position: absolute; border-radius: 50%; }
</style>
</head>
<body>
<main class="sheet">

  <!-- Concept 1: blue -->
  <section class="card card--blue" style="left:55px; top:55px;">
    <div class="hand-art" role="img" aria-label="Black silhouette of an arm swinging a hammer" style="left:0; top:0; width:290px; height:212px; background: linear-gradient(100deg, var(--black) 0%, var(--black) 28%, rgba(0,0,0,0) 29%), linear-gradient(180deg, var(--black) 0 22%, rgba(0,0,0,0) 22%) 60px 60px / 200px 40px no-repeat;"></div>
    <div class="abs mark mark--initials" style="left:203px; top:118px; color:var(--white);">P B P</div>
    <div class="abs mark mark--name" style="left:122px; top:176px; color:var(--white);">Pemberton Building Partners</div>
  </section>
  <span class="side-label" style="left:60px; top:284px;">Front</span>

  <section class="card card--black" style="left:491px; top:55px;">
    <div class="hand-art" role="img" aria-label="Blue silhouette of a hand holding a hammer" style="left:0; top:0; width:145px; height:56px; background: linear-gradient(90deg, var(--blue) 0 55%, rgba(31,110,173,0.85) 100%);"></div>
    <div class="abs mark mark--initials-sm" style="left:86px; top:66px; color:var(--blue);">P B P</div>
    <div class="abs mark mark--name-sm" style="left:29px; top:106px; color:var(--blue);">Pemberton Building Partners</div>
    <div class="web" style="left:88px; top:183px; color:var(--white);">www. pbp.com.au</div>
    <div class="contact" style="left:244px; top:24px;">
      <div class="person">Liam Carver</div>
      <div class="role">Contractor</div>
      <div class="address">4/2815 Harper Street<br>Brisbane QLD 4000<br>Northgate QLD 4013</div>
      <dl class="details">
        <dt>ABN No :</dt><dd class="strong">031927485</dd>
        <dt>Phone:</dt><dd>07 3118 2650</dd>
        <dt>Fax :</dt><dd>07 3118 2650</dd>
        <dt>Mobile :</dt><dd>912467305</dd>
      </dl>
      <div class="email">liamcarver@pbp.com.au</div>
    </div>
  </section>
  <span class="side-label" style="left:494px; top:289px;">Back</span>

  <!-- Concept 2: yellow -->
  <section class="card card--yellow" style="left:55px; top:330px;">
    <div class="hand-art" role="img" aria-label="Black silhouette of an arm swinging a hammer" style="left:0; top:0; width:290px; height:212px; background: linear-gradient(100deg, var(--black) 0%, var(--black) 28%, rgba(0,0,0,0) 29%), linear-gradient(180deg, var(--black) 0 22%, rgba(0,0,0,0) 22%) 60px 60px / 200px 40px no-repeat;"></div>
    <div class="abs mark mark--initials" style="left:203px; top:118px; color:var(--black);">P B P</div>
    <div class="abs mark mark--name" style="left:122px; top:176px; color:var(--black);">Pemberton Building Partners</div>
  </section>
  <span class="side-label" style="left:55px; top:562px;">Front</span>

  <section class="card card--black" style="left:491px; top:330px;">
    <div class="hand-art" role="img" aria-label="Yellow silhouette of a hand holding a hammer" style="left:0; top:0; width:145px; height:56px; background: linear-gradient(90deg, var(--yellow) 0 55%, rgba(252,210,0,0.85) 100%);"></div>
    <div class="abs mark mark--initials-sm" style="left:86px; top:66px; color:var(--yellow);">P B P</div>
    <div class="abs mark mark--name-sm" style="left:29px; top:106px; color:var(--yellow);">Pemberton Building Partners</div>
    <div class="web" style="left:88px; top:183px; color:var(--yellow);">www. pbp.com.au</div>
    <div class="contact contact--gold" style="left:244px; top:24px;">
      <div class="person">Liam Carver</div>
      <div class="role">Contractor</div>
      <div class="address">4/2815 Harper Street<br>Brisbane QLD 4000<br>Northgate QLD 4013</div>
      <dl class="details">
        <dt>ABN No :</dt><dd class="strong">031927485</dd>
        <dt>Phone:</dt><dd>07 3118 2650</dd>
        <dt>Fax :</dt><dd>07 3118 2650</dd>
        <dt>Mobile :</dt><dd>912467305</dd>
      </dl>
      <div class="email">liamcarver@pbp.com.au</div>
    </div>
  </section>
  <span class="side-label" style="left:482px; top:567px;">Back</span>

  <!-- Concept 3: saw -->
  <section class="card card--yellow" style="left:55px; top:622px;">
    <div class="abs mark mark--initials" style="left:70px; top:72px; color:var(--black);">P B P</div>
    <div class="abs mark mark--name" style="left:35px; top:139px; font-size:15.5px; color:var(--black);">Pemberton Building Partners</div>
    <div class="saw-art" role="img" aria-label="White circular saw blade with yellow centre" style="left:258px; top:-27px; width:240px; height:240px; background: radial-gradient(circle, var(--yellow) 0 33%, var(--white) 34%);"></div>
  </section>
  <span class="side-label" style="left:74px; top:867px;">Front</span>

  <section class="card card--black" style="left:496px; top:624px;">
    <div class="contact contact--gold" style="left:43px; top:19px;">
      <div class="person">Liam Carver</div>
      <div class="role">Contractor</div>
      <div class="address">4/2815 Harper Street<br>Brisbane QLD 4000<br>Northgate QLD 4013</div>
      <dl class="details">
        <dt>ABN No :</dt><dd class="strong">031927485</dd>
        <dt>Phone:</dt><dd>07 3118 2650</dd>
        <dt>Fax :</dt><dd>07 3118 2650</dd>
        <dt>Mobile :</dt><dd>912467305</dd>
      </dl>
      <div class="email">liamcarver@pbp.com.au</div>
    </div>
    <div class="saw-art" role="img" aria-label="Yellow circular saw blade with black centre" style="left:248px; top:-22px; width:256px; height:256px; background: radial-gradient(circle, var(--black) 0 45%, var(--yellow) 46%);"></div>
  </section>
  <span class="side-label" style="left:502px; top:865px;">Back</span>

  <!-- Concept 4: white and black -->
  <section class="card card--white" style="left:55px; top:922px;">
    <div class="abs mark mark--initials" style="left:40px; top:58px; color:var(--black);">P B P</div>
    <div class="abs mark" style="left:38px; top:112px; font-size:15px; line-height:19px; color:var(--black); white-space:normal; width:150px;">Pemberton Building Partners</div>
    <div class="abs" style="left:225px; top:0; width:160px; height:212px; background:var(--black);"></div>
    <div class="contact contact--gold" style="left:248px; top:18px;">
      <div class="person">Liam Carver</div>
      <div class="role">Contractor</div>
      <div class="address">4/2815 Harper Street<br>Brisbane QLD 4000<br>Northgate QLD 4013</div>
      <dl class="details">
        <dt>ABN No :</dt><dd class="strong">031927485</dd>
        <dt>Phone:</dt><dd>07 3118 2650</dd>
        <dt>Fax :</dt><dd>07 3118 2650</dd>
        <dt>Mobile :</dt><dd>912467305</dd>
      </dl>
      <div class="email">liamcarver@pbp.com.au</div>
    </div>
  </section>

  <section class="card card--black" style="left:492px; top:922px;">
    <div class="abs mark mark--initials" style="left:126px; top:52px; color:var(--yellow);">P B P</div>
    <div class="abs mark" style="left:120px; top:112px; font-size:17px; line-height:21px; color:var(--yellow); white-space:normal; width:160px;">Pemberton Building Partners</div>
  </section>

</main>
</body>
</html>
```